Brochure and Banner Designs

We need to put the attached brochure in a very professional, intriguing and relaxing to read and interest follow up...we would like to work with the colours of our logo...the brown stands for healthy homes, the blue for engaged communities and the green for natural surroundings. We bought the pic in the brochure. We would like to see the kid with the puff in a transparent background to minimize distraction. Also we would like the picture to blend beautifully with the background. We have used a template with an idea if what we are looking for.

We also need a banner design. I have attached the idea as well. I also attached the logo of the company so you can play with ideas around it. The 3d pic is not final, we will receive it next week, for now lets leave the space for it and work on the look and the information...we thought about add the colours that belong to each pillar as indicated in the paragraph above. It could be kind of abstract...blending each colour in the transition...Please note that I included a closer pic of the buildings, since it could be blended with the aerial view. As indicated before the aerial view is draft for now.

Any way good lock and I will asssit all your questions....

Lucia
Updates

Please note that for the banner, we were advised that people will only have 3 seconds to see it (sicne they will be driving)...so to simplify the message, it was suggested removing the description under each pillar...so lets only leave:

Maison saines
Collectivité bienveillante
Cadre de vie naturel

Thanks,
Lucia

Please when write Le Verger on the top of the banner, please ensure is written as the file I just attached to the fiel for your information.

Hi, everyone...

                                 

Thanks for your time and ideas!

Lucia

Hi, Guys

Could you please confirm who is planning to submit designs..?

Thanks,

Lucia

I hope to receive more designs...

Lucia

                                       

1058924 Preferred front cover (only comment too beige) and center as for the family suggested the building behind the family and replaced the kids by the family in this design.

The vision and mission exchange position with the Do you know…for this page suggested removing the kid with the puff and using the asthma kid as a backgrounder as it is done in design 1066529 but only covering this page and making the asthma puff more evident. This will provide more space for text in that page. The vision and mission as design 1066529.

Proactive Approach on center inside line to be removed…so on the top of this page Healthy Homes..pics are preferred squared..

The engaged community pic has been change for the grandpa with kids around. Attached in the file.

As for the banner, it is considered too blue…please follow the background use for brochure cover for design 1058924. As for the website only use tormelio.com do not write tormelio twice. Pleas edo not use bullets for the elements…

Thanks for your participation!

Lucia

                                   

the tree as a background is vey nice...

Target Market(s)

Highly educated people specially women 35-55 years old $70K plus salaries

Industry/Entity Type

It Company

Requirements
Must have
• The logo
All the info included in the attachements...ideas are welcome on the language, structure, flow, colours, etc...
Nice to have
• Nice flow...focus points.
Should not have
• non earth colours

```html
<!DOCTYPE html>
<html lang="en">
<head>
<meta charset="utf-8">
<title>tormelio – Balanced, Local Homesteads brochure</title>
<link href="https://fonts.googleapis.com/css2?family=Carlito:wght@400;700&family=Cinzel:wght@400&display=swap" rel="stylesheet">
<style>
  :root{
    --gold:#c7b37a;
    --brown:#6b5634;
    --brown-dark:#4a3a1e;
    --text:#4a3b22;
    --green:#b3c84f;
    --olive:#c2ab5e;
    --blue:#5b97c8;
    --fold:#8a7446;
    --paper:#ffffff;
  }
  *{margin:0;padding:0;box-sizing:border-box}
  html,body{width:1200px;height:849px;overflow:hidden;background:var(--paper)}
  .brochure{position:relative;width:1200px;height:849px;overflow:hidden;background:
    radial-gradient(ellipse 420px 520px at 590px 360px, rgba(226,219,200,.35), rgba(255,255,255,0) 70%),
    var(--paper);font-family:"Carlito",Calibri,Arial,sans-serif;color:var(--text)}
  .band{position:absolute;left:0;width:1200px}
  .band--top{top:0;height:90px}
  .band--bottom{bottom:0;height:80px}
  .fold{position:absolute;top:0;height:849px;width:0;border-left:1.5px dashed var(--fold);opacity:.8}
  .fold--one{left:392px}
  .fold--two{left:797px}

  /* left panel */
  .photo-child{position:absolute;left:0;top:500px;width:392px;height:349px;
    background:linear-gradient(to top, #b9a48c 0%, #d8c7b4 45%, rgba(238,228,218,0) 100%)}
  .facts{position:absolute;left:28px;top:74px;width:336px}
  .facts__title{font-weight:700;font-size:22px;color:var(--brown-dark);text-align:center;letter-spacing:.3px}
  .facts__rule{height:6px;margin:6px 20px 22px;background:radial-gradient(circle,var(--green) 2px,transparent 2.4px) 0 0/9px 6px repeat-x}
  .facts p{font-size:15px;line-height:19.5px;text-align:justify;margin-bottom:16px}
  .facts p:first-of-type{margin-bottom:24px}

  /* name blocks */
  .brand{position:absolute;text-align:center;color:var(--brown)}
  .brand__name{font-weight:700;line-height:1;letter-spacing:.5px}
  .brand__tag{font-size:11px;margin-top:5px}
  .brand__mark{display:inline-block;width:10px;height:10px;background:var(--brown);margin-right:8px;vertical-align:middle}
  .brand--back{left:495px;top:572px;width:200px}
  .brand--back .brand__name{font-size:40px}
  .brand--cover{left:880px;top:184px;width:240px}
  .brand--cover .brand__name{font-size:48px}
  .brand--cover .brand__tag{font-size:12.5px}

  .contact{position:absolute;left:495px;top:644px;width:200px;text-align:center;font-size:15px;line-height:19px;color:var(--brown-dark);font-style:normal}

  .gallery{position:absolute;left:805px;top:282px;width:385px;height:320px}

  .cover-title{position:absolute;left:815px;top:620px;width:370px;text-align:center;font-family:"Cinzel",Georgia,serif;font-weight:400;font-size:36px;line-height:39px;letter-spacing:1px}
  .cover-title span{display:block}
  .t-green{color:var(--green)}
  .t-olive{color:var(--olive)}
  .t-blue{color:var(--blue)}
</style>
</head>
<body>
<main class="brochure">
  <svg class="band band--top" viewBox="0 0 1200 90" preserveAspectRatio="none" aria-hidden="true">
    <defs>
      <linearGradient id="topGold" x1="0" x2="1" y1="0" y2="0">
        <stop offset="0" stop-color="#c6b27a"/>
        <stop offset=".45" stop-color="#f1ead5"/>
        <stop offset=".7" stop-color="#d9c89a"/>
        <stop offset="1" stop-color="#c4ae72"/>
      </linearGradient>
    </defs>
    <path d="M0 0H1200V48C1080 28 960 22 800 30C640 38 520 14 380 16C230 18 110 46 0 40Z" fill="url(#topGold)"/>
    <path d="M0 40C110 46 230 18 380 16C520 14 640 38 800 30C960 22 1080 28 1200 48" fill="none" stroke="#fff" stroke-width="3" opacity=".8"/>
  </svg>

  <svg class="band band--bottom" viewBox="0 0 1200 80" preserveAspectRatio="none" aria-hidden="true">
    <defs>
      <linearGradient id="bottomBrown" x1="0" x2="1" y1="0" y2="0">
        <stop offset="0" stop-color="#5e4a2b"/>
        <stop offset=".35" stop-color="#8b7450"/>
        <stop offset=".5" stop-color="#e9e1cf"/>
        <stop offset=".7" stop-color="#a18a60"/>
        <stop offset="1" stop-color="#6b5634"/>
      </linearGradient>
    </defs>
    <path d="M0 30C160 8 330 10 520 26C700 40 900 20 1060 14C1120 12 1170 16 1200 22V80H0Z" fill="url(#bottomBrown)"/>
    <path d="M0 30C160 8 330 10 520 26C700 40 900 20 1060 14C1120 12 1170 16 1200 22" fill="none" stroke="#fff" stroke-width="3" opacity=".85"/>
  </svg>

  <div class="photo-child" role="img" aria-label="Photo of a young boy breathing through an asthma inhaler mask, fading into the page"></div>
  <section class="facts">
    <h2 class="facts__title">DO YOU KNOW…</h2>
    <div class="facts__rule"></div>
    <p>A leading global health body describes health as a state of complete physical, mental, and social wellbeing, not simply the absence of disease or infirmity.</p>
    <p>According to a national allergy and air quality council, 50% of all illnesses are either caused or aggravated by poor indoor air quality.</p>
    <p>61% of Canada’s fresh water is rated fair, marginal or poor due to physical, microbiological, chemical, and/ or radiological contaminants.</p>
    <p>Many researchers believe that interpersonal relationships are the most crucial factor to overall health.</p>
    <p>A growing body of scientific evidence indicates that being with or even looking at nature – particularly in its wild state - produces positive physical, mental, social and spiritual benefits.</p>
  </section>

  <div class="fold fold--one"></div>
  <div class="fold fold--two"></div>

  <div class="brand brand--back">
    <div class="brand__name"><span class="brand__mark"></span>tormelio</div>
    <div class="brand__tag">Balanced, Local Homesteads</div>
  </div>
  <address class="contact">
    1487 Rue des Érables<br>
    PO 52170 Hull<br>
    Gatineau&nbsp; QC<br>
    J9A 4P2<br>
    819-555-0172<br>
    info@tormelio.com<br>
    TORMELIO.COM
  </address>

  <div class="brand brand--cover">
    <div class="brand__name"><span class="brand__mark"></span>tormelio</div>
    <div class="brand__tag">Balanced, Local Homesteads</div>
  </div>

  <svg class="gallery" viewBox="0 0 385 320">
    <defs>
      <linearGradient id="forest" x1="0" x2="1" y1="0" y2="1">
        <stop offset="0" stop-color="#c9b04a"/><stop offset="1" stop-color="#5c6a2a"/>
      </linearGradient>
      <linearGradient id="lake" x1="0" x2="0" y1="0" y2="1">
        <stop offset="0" stop-color="#8fb2cf"/><stop offset=".6" stop-color="#a99a7c"/><stop offset="1" stop-color="#6e5a3c"/>
      </linearGradient>
      <linearGradient id="autumn" x1="0" x2="1" y1="0" y2="1">
        <stop offset="0" stop-color="#e0a93a"/><stop offset=".6" stop-color="#b34a2a"/><stop offset="1" stop-color="#6b5a2a"/>
      </linearGradient>
    </defs>
    <g role="img" aria-label="Photo of a young woman jogging through a green park">
      <polygon points="48,2 140,2 188,88 140,174 48,174 0,88" fill="url(#forest)"/>
    </g>
    <g role="img" aria-label="Photo of a grandfather and child sitting on a wooden dock by a lake">
      <polygon points="243,2 335,2 383,88 335,174 243,174 195,88" fill="url(#lake)"/>
    </g>
    <g role="img" aria-label="Photo of two smiling children in autumn woods">
      <polygon points="146,146 238,146 286,232 238,318 146,318 98,232" fill="url(#autumn)"/>
    </g>
  </svg>

  <h1 class="cover-title">
    <span class="t-green">BALANCED</span>
    <span class="t-olive">LOCAL</span>
    <span class="t-blue">HOMESTEADS</span>
  </h1>
</main>
</body>
</html>
```